Kestrel Photography Business Card

I need a business card designed for a photography business based in Perth, Western Australia called Kestrel Photography.

We specialise in wedding, event photography and portrait photography.

The business card must borrow the style of the attached logo.

The hex codes for the colours in the logo are:
#ED1D85 - Pink
#89C23E - Green
#37282F - Black

The name on the card will be:
Name: Torvane
Phone: 0417395286
Website: www.kestrelphotography.example.au
Social: kestrelphotography

I am open and happy to accept creative concepts.

I’d like some space at the back for writing notes and appointment details.

```html
<!DOCTYPE html>
<html lang="en">
<head>
<meta charset="utf-8">
<title>Kestrel Photography Business Card</title>
<link rel="stylesheet" href="https://fonts.googleapis.com/css2?family=Open+Sans:wght@300;400&display=swap">
<style>
  :root {
    --pink: #ED1D85;
    --green: #89C23E;
    --ink: #37282F;
    --card-dark: #222325;
    --card-light: #ffffff;
    --backdrop: #dcdcdc;
    --text-light: #f2f2f2;
  }
  * { margin: 0; padding: 0; box-sizing: border-box; }
  html, body {
    width: 1200px;
    height: 748px;
    overflow: hidden;
    background: var(--backdrop);
    font-family: "Open Sans", Arial, sans-serif;
  }
  .canvas {
    position: relative;
    width: 1200px;
    height: 748px;
  }
  .card {
    position: absolute;
    top: 220px;
    width: 540px;
    height: 309px;
    box-shadow: 0 6px 18px rgba(0, 0, 0, 0.18);
  }
  .card-front {
    left: 40px;
    background: var(--card-light);
    display: flex;
    flex-direction: column;
    align-items: center;
    justify-content: center;
    gap: 34px;
  }
  .brand-mark {
    width: 96px;
    height: 96px;
    border-radius: 50%;
    background: var(--pink);
  }
  .brand-name {
    color: var(--ink);
    font-weight: 400;
    font-size: 17px;
    letter-spacing: 0.62em;
    text-transform: uppercase;
    margin-right: -0.62em;
  }
  .card-back {
    left: 620px;
    background: var(--card-dark);
    padding: 0 34px;
    display: flex;
    flex-direction: column;
    align-items: flex-end;
    justify-content: center;
    text-align: right;
  }
  .person-name {
    color: var(--pink);
    font-size: 22px;
    line-height: 1.2;
  }
  .person-role {
    color: var(--green);
    font-size: 27px;
    line-height: 1.2;
    margin-bottom: 12px;
  }
  .contact-line {
    color: var(--text-light);
    font-size: 15.5px;
    line-height: 1.45;
  }
</style>
</head>
<body>
  <main class="canvas">
    <section class="card card-front">
      <div class="brand-mark"></div>
      <div class="brand-name">Kestrel Photography</div>
    </section>
    <section class="card card-back">
      <p class="person-name">Torvane</p>
      <p class="person-role">photographer</p>
      <p class="contact-line">Phone: 0417395286</p>
      <p class="contact-line">Website: www.kestrelphotography.example.au</p>
      <p class="contact-line">Social: kestrelphotography</p>
    </section>
  </main>
</body>
</html>
```